Flyer for photo scanning business

Hello,
I need a flyer created for my business that would be suitable for print, to drop in letterboxes in my local community.

I would like the flyer to convey very simply the services I offer which is scanning negatives, slides and VHS tapes to digital files.
Hopefully it can make it look like an easy process, as people are often daunted by the task of sorting through old photos so they don't always get around to having them scanned.

I have a pinned facebook post that can be used by the designer to reference my services. Pricing does not need to be included on the flyer.
http://facebook.com/lanternloftmedia

Target Market(s)

Parents & Grandparents

Requirements
Must have
• Must make my services look simple! Refer to pinned facebook post for detailed outline of my services.

I would like to flyer to point towards my contact details -
www.lanternloft.com
Miriam 0482 917 356

Colours in line with my logo/brand (uploaded to brief).
Nice to have
• Stock images of 35mm film negatives, 8mm film, VHS tapes, or Velmaprint slides would be worth including. I have also uploaded a mockup of the USB sticks that I provide with digitised images.
Should not have
• no prices needed,

```html
<!DOCTYPE html>
<html lang="en">
<head>
<meta charset="UTF-8">
<title>Lantern Loft Media – Flyer</title>
<link rel="stylesheet" href="https://fonts.googleapis.com/css2?family=Raleway:wght@400;500;700&display=swap">
<style>
  :root {
    --brand-blue: #2b6199;
    --rule-blue: #6f93bb;
    --ink: #111111;
    --paper: #ffffff;
    --photo-top: #c8463a;
    --photo-mid: #3f7fae;
    --photo-deep: #1b1e30;
  }
  * { margin: 0; padding: 0; box-sizing: border-box; }
  html, body { width: 927px; height: 1200px; overflow: hidden; background: var(--paper); }
  body { font-family: "Raleway", sans-serif; color: var(--ink); font-variant-numeric: lining-nums; }

  .flyer { position: relative; width: 927px; height: 1200px; background: var(--paper); }

  .hero-photo {
    position: absolute; left: 0; top: 0; width: 469px; height: 1200px;
    background:
      linear-gradient(180deg,
        var(--photo-top) 0%,
        #d8b23a 18%,
        var(--photo-mid) 32%,
        #2a2c3d 44%,
        #3a3540 47%,
        var(--photo-deep) 62%,
        #2c2a36 85%,
        #8d8a84 100%);
  }

  .brand-name {
    position: absolute; left: 520px; width: 360px; text-align: center;
    color: var(--brand-blue); font-weight: 500; text-transform: uppercase;
    white-space: nowrap; line-height: 1;
  }
  .brand-name--main { top: 258px; font-size: 36px; letter-spacing: 5px; }
  .brand-name--sub { top: 312px; font-size: 24px; letter-spacing: 6px; }

  .about { position: absolute; left: 531px; top: 398px; width: 345px; }
  .about__title { color: var(--brand-blue); font-size: 18px; font-weight: 700; margin-bottom: 19px; }
  .about__text { font-size: 16px; line-height: 22px; font-weight: 500; }

  .rule {
    position: absolute; left: 531px; width: 326px; height: 1px; background: var(--rule-blue);
  }
  .rule::before {
    content: ""; position: absolute; left: 0; top: -1px; width: 68px; height: 3px;
    background: var(--brand-blue);
  }

  .step-badge {
    position: absolute; left: 433px; width: 68px; height: 68px; border-radius: 50%;
    background: var(--brand-blue); border: 3px solid var(--paper);
    display: flex; align-items: center; justify-content: center;
  }

  .step { position: absolute; left: 531px; width: 275px; }
  .step__label { color: var(--brand-blue); font-size: 19px; font-weight: 700; margin-bottom: 20px; }
  .step__text { font-size: 16px; line-height: 22px; font-weight: 500; }

  .contact { position: absolute; left: 531px; top: 1131px; font-size: 11px; font-weight: 500; white-space: nowrap; }
</style>
</head>
<body>
<main class="flyer">
  <div class="hero-photo" role="img" aria-label="Close-up photo of a pile of coloured plastic slide mounts above rolls of 35mm film negatives and canisters"></div>

  <div class="brand-name brand-name--main">Lantern Loft</div>
  <div class="brand-name brand-name--sub">Media</div>

  <section class="about">
    <h2 class="about__title">About us</h2>
    <p class="about__text">Lantern Loft Media is a small business run from my home in the Perth Hills. I digitise photos that haven't been seen in years, bringing them back to life.</p>
  </section>

  <div class="rule" style="top:579px"></div>
  <div class="step-badge" style="top:580px">
    <svg width="34" height="34" viewBox="0 0 34 34" fill="none" stroke="#fff" stroke-width="1.6">
      <rect x="3" y="3" width="28" height="28"/>
      <line x1="3" y1="8" x2="31" y2="8"/>
      <line x1="3" y1="26" x2="31" y2="26"/>
      <rect x="9" y="11" width="16" height="12"/>
      <g stroke-width="1.2">
        <line x1="6" y1="5.5" x2="8" y2="5.5"/><line x1="11" y1="5.5" x2="13" y2="5.5"/><line x1="16" y1="5.5" x2="18" y2="5.5"/><line x1="21" y1="5.5" x2="23" y2="5.5"/><line x1="26" y1="5.5" x2="28" y2="5.5"/>
        <line x1="6" y1="28.5" x2="8" y2="28.5"/><line x1="11" y1="28.5" x2="13" y2="28.5"/><line x1="16" y1="28.5" x2="18" y2="28.5"/><line x1="21" y1="28.5" x2="23" y2="28.5"/><line x1="26" y1="28.5" x2="28" y2="28.5"/>
      </g>
    </svg>
  </div>
  <section class="step" style="top:592px">
    <h3 class="step__label">STEP 1</h3>
    <p class="step__text">Find your old negatives or tapes and organise them as much or as little as you want.</p>
  </section>

  <div class="rule" style="top:716px"></div>
  <div class="step-badge" style="top:716px">
    <svg width="34" height="34" viewBox="0 0 34 34" fill="none" stroke="#fff" stroke-width="1.6" stroke-linejoin="round">
      <path d="M3 14 L17 4 L31 14 V30 H3 Z"/>
      <path d="M7 17 V9 H27 V17"/>
      <path d="M3 14 L17 24 L31 14"/>
      <path d="M3 30 L14 21.5 M31 30 L20 21.5"/>
      <line x1="11" y1="12" x2="23" y2="12"/><line x1="11" y1="16" x2="23" y2="16"/>
    </svg>
  </div>
  <section class="step" style="top:726px">
    <h3 class="step__label">STEP 2</h3>
    <p class="step__text">E-mail miriam@lanternloft.com and i will come and collect these from your home in the hills area.</p>
  </section>

  <div class="rule" style="top:851px"></div>
  <div class="step-badge" style="top:852px">
    <svg width="36" height="32" viewBox="0 0 36 32" fill="none" stroke="#fff" stroke-width="1.6" stroke-linejoin="round">
      <path d="M2 4 H13 L16 8 H34 V29 H2 Z"/>
      <line x1="2" y1="12" x2="34" y2="12"/>
    </svg>
  </div>
  <section class="step" style="top:861px">
    <h3 class="step__label">STEP 3</h3>
    <p class="step__text">Once completed (usually within a few days) i will drop back your box of memories with a USB stick containing high resolution JPEG files. Contactless payment will be processed when i arrive.</p>
  </section>

  <div class="rule" style="top:1051px"></div>

  <p class="contact">Contact: Miriam 0482 917 356 | www.lanternloft.com</p>
</main>
</body>
</html>
```